Harwick Legal

To update and modernize current business card appearance. Marta's business is based in Melbourne with 4 other lawyers in the firm. Marta travels to the Pilbara in Western Australia approximately 1 week a month as part of the firms legal work. She consults with clients in Newman, Tom Price and Port Hedland. The lawyers work mostly from a home office, apart from court appearances. They have a virtual office in Melbourne city, and use facilities in 3 or 4 other locations around Melbourne. It is important the client's think this is a conventional law firm with a permanent office. Our business structure is a difficult concept for them to grasp. The business has been operational for 3 years, growing from 1 lawyer to 4 lawyers during that time. Our website is www.Harwicklegal.example.au and is currently being upgraded as we are not happy with its content. The logo is currently orange and dark grey but the orange is a difficult colour to reproduce and often turns out "poo" brown when documents are printed. We need clients to know we are user friendly and caring - and not head up our rears ends as some lawyers appear to be.
Updates

Thank you for the feedback so far. 1. Some of the designs have too much black (We prefer darker grey & not too much.) 2. Happy for designers to play around with different colours & logo design. What we're after is a modern look and business card that people say "wow" when they pick it up.

Industry/Entity Type

Business

```html
<!DOCTYPE html>
<html lang="en">
<head>
<meta charset="utf-8">
<title>Harwick Legal – Business Card</title>
<link rel="stylesheet" href="https://fonts.googleapis.com/css2?family=Cinzel:wght@400;600;700&family=Jost:wght@300;400&display=swap">
<style>
  :root {
    --orange: #f28a37;
    --ink: #1c1c1c;
    --slate: #3a3c3f;
    --rule: #2a2a2a;
    --paper: #ffffff;
    --canvas: #ffffff;
  }
  html, body {
    margin: 0;
    width: 1200px;
    height: 900px;
    overflow: hidden;
    background: var(--canvas);
  }
  .sheet {
    position: relative;
    width: 1200px;
    height: 900px;
  }
  .card {
    position: absolute;
    top: 249px;
    width: 472px;
    height: 264px;
    filter: drop-shadow(5px 6px 5px rgba(0,0,0,0.3));
  }
  .card--back { left: 91px; }
  .card--front { left: 645px; }
  .card svg { display: block; width: 100%; height: 100%; }
  .serif { font-family: "Cinzel", serif; }
  .sans { font-family: "Jost", sans-serif; }
  .fill-orange { fill: var(--orange); }
  .fill-ink { fill: var(--ink); }
  .fill-slate { fill: var(--slate); }
  .fill-paper { fill: var(--paper); }
  .stroke-rule { stroke: var(--rule); }
</style>
</head>
<body>
<main class="sheet">

  <section class="card card--back" aria-label="Business card back, areas of practice">
    <svg viewBox="0 0 413 231" xmlns="http://www.w3.org/2000/svg">
      <rect class="fill-paper stroke-rule" x="0.5" y="0.5" width="412" height="230" stroke-width="1"/>
      <polygon class="fill-orange" points="0,69 4,69 120,194 0,194"/>
      <polygon class="fill-orange" points="413,69 409,69 307,194 413,194"/>
      <line class="stroke-rule" x1="0" y1="54" x2="118" y2="54" stroke-width="1.2"/>
      <line class="stroke-rule" x1="295" y1="54" x2="413" y2="54" stroke-width="1.2"/>

      <g class="brand-mark">
        <circle class="fill-orange" cx="375" cy="19" r="8"/>
        <text class="serif fill-ink" x="375" y="39" font-size="7" font-weight="700" text-anchor="middle">HARWICK LEGAL</text>
      </g>

      <text class="serif fill-ink" x="206" y="59" font-size="15" font-weight="600" text-anchor="middle" letter-spacing="0.4">AREAS OF PRACTICE:</text>

      <text class="serif fill-ink" x="206" y="82" font-size="11" font-weight="600" text-anchor="middle">• Family Law</text>
      <text class="serif fill-ink" x="206" y="100" font-size="8.5" text-anchor="middle" letter-spacing="1">Collaborative Practice</text>
      <text class="serif fill-ink" x="206" y="112" font-size="8.5" text-anchor="middle" letter-spacing="1">Mediation &amp; Negotiation</text>
      <text class="serif fill-ink" x="206" y="124" font-size="8.5" text-anchor="middle" letter-spacing="1">Intervention Orders</text>

      <text class="serif fill-ink" x="206" y="156" font-size="11" font-weight="600" text-anchor="middle">• Criminal Law</text>

      <text class="sans fill-ink" x="206" y="186" font-size="8.5" font-weight="300" text-anchor="middle">Inquiries:  info@harwicklegal.example.au</text>

      <rect class="fill-slate" x="0" y="194" width="413" height="37"/>
      <text class="serif fill-orange" x="206" y="210" font-size="9.5" text-anchor="middle" letter-spacing="0.5">EXPERIENCE - SUPPORT - SOLUTIONS</text>
    </svg>
  </section>

  <section class="card card--front" aria-label="Business card front, solicitor details">
    <svg viewBox="0 0 413 231" xmlns="http://www.w3.org/2000/svg">
      <rect class="fill-paper stroke-rule" x="0.5" y="0.5" width="412" height="230" stroke-width="1"/>
      <polygon class="fill-orange" points="0,69 105,69 125,92 288,92 308,69 413,69 413,194 0,194"/>
      <line class="stroke-rule" x1="0" y1="78" x2="113" y2="78" stroke-width="1.2"/>
      <line class="stroke-rule" x1="300" y1="78" x2="413" y2="78" stroke-width="1.2"/>
      <polygon class="fill-slate" points="0,105 95,194 0,194"/>
      <polygon class="fill-slate" points="413,105 318,194 413,194"/>

      <g class="brand-mark">
        <circle class="fill-orange" cx="206" cy="30" r="15"/>
        <text class="serif fill-ink" x="206" y="64" font-size="13" font-weight="700" text-anchor="middle">HARWICK LEGAL</text>
      </g>

      <text class="serif fill-ink" x="206" y="117" font-size="16" font-weight="600" text-anchor="middle">J. Marta Corran</text>
      <text class="sans fill-ink" x="206" y="128" font-size="6.8" text-anchor="middle">LLB(Hons), Dip Pro Mgt - Accredited Mediator</text>
      <text class="serif fill-ink" x="206" y="146" font-size="9.5" font-weight="700" text-anchor="middle">Principal Solicitor</text>
      <text class="sans fill-ink" x="206" y="164" font-size="7.4" text-anchor="middle">t: 1300 HARWICK (1300 427 942)</text>
      <text class="sans fill-ink" x="206" y="174" font-size="7.4" text-anchor="middle">m: 0400 555 019</text>
      <text class="sans fill-ink" x="206" y="184" font-size="7.4" text-anchor="middle">e: marta.corran@harwicklegal.example.au</text>

      <rect class="fill-orange" x="0" y="194" width="413" height="2.5"/>
      <rect class="fill-slate" x="0" y="196.5" width="413" height="34.5"/>
      <text class="serif fill-orange" x="206" y="209" font-size="8.5" text-anchor="middle" letter-spacing="0.5">Serving the People of the Pilbara</text>
      <polygon class="fill-orange" points="126,216 288,216 270,231 145,231"/>
    </svg>
  </section>

</main>
</body>
</html>
```